IT Consulting TorvendaleNetInc.example needs Simple and Neat WebDesigns

We are a IT consulting business, currently needing a logo and a neat website that looks simple and attractive. If could be creative enough to come up with something that follows these guidelines.
We are talking about 10-15 static pages here

1. Nice and Neat
2. Color consistancy
3. Latest menu bars
4. Easy cross navigation
5. Less Maintenance
6. Easy upgrades
Updates

Reason: new to this and getting familiar with the time I have onhand

Reason: I want to give more time to get good quality

Reason: inviting more designs

Target Market(s)

IT services and consulting - should look very very professional and elegant.

Industry/Entity Type

Business

Requirements
Must have
• I would like to receive the best designs for our website
Nice to have
• Design a good logo to go with the website

```html
<!DOCTYPE html>
<html lang="en">
<head>
<meta charset="utf-8">
<title>Torvendale Inc. – IT Consulting</title>
<link rel="stylesheet" href="https://fonts.googleapis.com/css2?family=Source+Sans+3:wght@400;600&family=Arimo:wght@400&display=swap">
<style>
:root{
  --page:#f0f6f6;
  --brand:#1b5c74;
  --brand-dark:#12566e;
  --accent:#3ba8b5;
  --nav:#151515;
  --ink:#5a5f62;
  --muted:#8a9ba2;
  --gold:#f2c46e;
  --rule:#c9d2d4;
}
*{margin:0;padding:0;box-sizing:border-box}
html,body{width:1200px;height:1130px;overflow:hidden;background:var(--page)}
.site{position:relative;width:1200px;height:1130px;overflow:hidden;background:var(--page);font-family:"Arimo",Arial,sans-serif}
.abs{position:absolute}
.brand{left:134px;top:84px;display:flex;align-items:center;gap:12px;font-family:"Source Sans 3",sans-serif;font-weight:600;font-size:38px;color:var(--brand);letter-spacing:0.5px}
.brand-dot{width:22px;height:22px;border-radius:50%;background:var(--accent)}
.phone{right:150px;top:98px;display:flex;align-items:center;gap:10px;font-family:"Source Sans 3",sans-serif;font-weight:600;font-size:28px;color:#7b9198}
.nav{left:0;top:151px;width:1200px;height:44px;background:var(--nav)}
.nav ul{list-style:none;display:flex;position:absolute;left:120px;top:7px}
.nav li{font-family:"Source Sans 3",sans-serif;font-weight:600;font-size:15px;color:#fff;height:30px;line-height:30px;padding:0 8px;margin-right:16px}
.nav li.is-active{background:var(--accent);border-radius:2px}
.hero-band{left:0;top:195px;width:1200px;height:396px;background:linear-gradient(#1c4f5c 0%,#6c8f97 35%,#dfe9ea 62%,var(--page) 75%)}
.hero-shadow{left:128px;top:558px;width:944px;height:26px;border-radius:50%;background:#000;filter:blur(4px)}
.hero{left:120px;top:216px;width:960px;height:350px;background:linear-gradient(160deg,#f3dbe8 0%,#b9dcfb 30%,#f4d3a8 52%,#ffffff 62%,#f7c6e0 80%,#b7c4f6 100%)}
.hero-title{left:669px;top:291px;font-family:"Source Sans 3",sans-serif;font-weight:600;font-size:31px;line-height:27px;color:var(--brand)}
.hero-sub{left:671px;top:350px;font-family:"Source Sans 3",sans-serif;font-weight:600;font-size:19px;color:#666}
.strip{left:0;top:591px;width:1200px;height:50px;border-top:1px solid #333;background:linear-gradient(#9ea6a8,var(--page))}
.follow{left:145px;top:609px;font-size:13px;color:#3b4b52;display:flex;align-items:center;gap:6px}
.social{width:16px;height:16px;background:#4d7fb3;border-radius:2px}
.social+.social{background:#5fb6d8}
.pager{left:988px;top:608px;display:flex;gap:5px}
.pager span{width:17px;height:17px;border-radius:50%;background:#1b1b1b}
.pager span:first-child{background:#3a3a3a}
.welcome{left:147px;top:666px;font-family:"Source Sans 3",sans-serif;font-size:26px;color:var(--brand)}
.intro{top:712px;font-size:12px;line-height:20px;letter-spacing:0.5px;color:var(--ink)}
.intro-left{left:147px;width:432px}
.intro-right{left:610px;width:440px}
.rule{left:146px;width:910px;height:1px;background:var(--rule)}
.footer-band{left:0;top:920px;width:1200px;height:210px;background:var(--brand-dark)}
.card{top:848px;width:290px;height:196px;background:linear-gradient(#e4ebec 0%,#b3c2c6 40%,#8fa2a7 100%);opacity:.93}
.card-title{position:absolute;top:14px;font-family:"Source Sans 3",sans-serif;font-weight:600;font-size:28px;color:var(--brand)}
.card-icon{position:absolute;left:6px;top:8px}
.card-text{position:absolute;left:8px;top:80px;width:272px;font-size:12px;line-height:20px;color:#fff;text-align:justify;letter-spacing:0.2px}
.card-more{position:absolute;right:14px;top:168px;font-size:12px;color:var(--gold)}
.copyright{right:154px;top:1084px;font-size:11px;color:#d4e2e7}
</style>
</head>
<body>
<div class="site">
  <div class="abs brand"><span class="brand-dot"></span>TORVENDALE Inc.</div>
  <div class="abs phone">
    <svg width="44" height="40" viewBox="0 0 44 40" aria-hidden="true">
      <ellipse cx="22" cy="36" rx="20" ry="3" fill="#c5cfd1"/>
      <path d="M4 12 Q22 -2 40 12 L36 18 L30 14 L30 10 Q22 7 14 10 L14 14 L8 18 Z" fill="#8ea2a8"/>
      <rect x="9" y="16" width="26" height="18" rx="3" fill="#8ea2a8"/>
      <circle cx="22" cy="25" r="6" fill="#e6ecee"/>
    </svg>
    (302) 555-0148
  </div>
  <nav class="abs nav">
    <ul>
      <li class="is-active">Home</li>
      <li>About Us</li>
      <li>Services</li>
      <li>Solutions</li>
      <li>Products</li>
      <li>Contact</li>
    </ul>
  </nav>
  <div class="abs hero-band"></div>
  <div class="abs hero-shadow"></div>
  <div class="abs hero" role="img" aria-label="Abstract flowing ribbons of blue, orange and pink light"></div>
  <h1 class="abs hero-title">Delivering World Class Data<br>Integration Solutions</h1>
  <div class="abs hero-sub">Header image 1 / 4</div>
  <div class="abs strip"></div>
  <div class="abs follow">Follow us&nbsp;<span class="social"></span><span class="social"></span></div>
  <div class="abs pager"><span></span><span></span><span></span><span></span></div>
  <h2 class="abs welcome">Welcome to Torvendale Inc.</h2>
  <p class="abs intro intro-left">Group of individuals who had passion for data warehouse and with great reputation and integrity. With over eighteen years of industry experience we are building an organization, Torvendale, from ground-up based on solid fundamentals, trust and commitment to provide quality service across various verticals.</p>
  <p class="abs intro intro-right">We believe that a reputation as an honest and reliable business is the recipe for success. While others seek to profit by cutting corners, or recommending unnecessary services to customers, Torvendale believe that a good reputation and consistent service will reap bigger profits in the long run.</p>
  <div class="abs rule" style="top:830px"></div>
  <div class="abs footer-band"></div>

  <section class="abs card" style="left:146px">
    <svg class="card-icon" width="62" height="56" viewBox="0 0 62 56" aria-hidden="true">
      <path d="M50 4 a14 14 0 1 0 8 18 l-10 -3 l-3 -8 z" fill="var(--accent)"/>
      <path d="M40 20 L4 48 L10 54 L46 26 Z" fill="var(--accent)"/>
    </svg>
    <h3 class="card-title" style="left:79px">Services</h3>
    <p class="card-text">Torvendale's will work with you to maximise the efficiency of your systems and processes and provide fully managed teams or individuals to ensure the successful delivery of your project.</p>
    <span class="card-more">read more »</span>
  </section>

  <section class="abs card" style="left:456px">
    <svg class="card-icon" width="62" height="60" viewBox="0 0 62 60" aria-hidden="true">
      <g fill="none" stroke="var(--accent)" stroke-width="3">
        <circle cx="32" cy="30" r="26"/>
        <ellipse cx="32" cy="30" rx="11" ry="26"/>
        <line x1="32" y1="4" x2="32" y2="56"/>
        <line x1="6" y1="30" x2="58" y2="30"/>
        <path d="M10 17 H54 M10 43 H54"/>
      </g>
    </svg>
    <h3 class="card-title" style="left:83px">Solutions</h3>
    <p class="card-text">Torvendale's experts will work in partnership with you and with our best of breed technology and offshore partners to deliver solutions that are cost effective, fit for purpose and highly scalable.</p>
    <span class="card-more">read more »</span>
  </section>

  <section class="abs card" style="left:766px">
    <svg class="card-icon" width="84" height="56" viewBox="0 0 84 56" aria-hidden="true">
      <g fill="var(--accent)">
        <circle cx="28" cy="34" r="14"/>
        <circle cx="58" cy="20" r="14"/>
        <g stroke="var(--accent)" stroke-width="6">
          <path d="M28 16 V52 M10 34 H46 M15 21 L41 47 M41 21 L15 47"/>
          <path d="M58 2 V38 M40 20 H76 M45 7 L71 33 M71 7 L45 33"/>
        </g>
      </g>
      <circle cx="28" cy="34" r="5" fill="#c9d4d6"/>
      <circle cx="58" cy="20" r="5" fill="#dbe3e4"/>
    </svg>
    <h3 class="card-title" style="left:100px">Products</h3>
    <p class="card-text">Torvendale's experts will work in partnership with you and with our best of breed technology and offshore partners to deliver solutions that are cost effective, fit for purpose and highly scalable.</p>
    <span class="card-more">read more »</span>
  </section>

  <div class="abs rule" style="top:1064px;background:#4f8597"></div>
  <div class="abs copyright">© Copyright TorvendaleNetInc.example &nbsp;All Rights Reserved</div>
</div>
</body>
</html>
```